Heating and Air Conditioning Company Needs a Business Card Design

Need a business card design for a company in South Carolina called "Larkfield Heating & Cooling LLC". We install, maintain, and repair HVAC systems and the bulk of our business is residential. We have a logo and are looking for a clean, professional looking card that resonates with "setting the standard for service and comfort".
Updates
Forgot to include this info - Licensed & Insured

Industry/Entity Type
Business

```html
<!DOCTYPE html>
<html lang="en">
<head>
<meta charset="utf-8">
<title>Larkfield Heating &amp; Cooling LLC — Business Card</title>
<link rel="stylesheet" href="https://fonts.googleapis.com/css2?family=Archivo:wght@700;800&family=Questrial&display=swap">
<style>
  :root {
    --backdrop: #2f3e46;
    --card: #ffffff;
    --band: #231f20;
    --ink: #1a1a1a;
    --ink-soft: #333333;
    --accent-red: #e8202a;
    --accent-blue: #1f5fae;
    --band-text: #f2f2f2;
  }
  * { box-sizing: border-box; margin: 0; padding: 0; }
  html, body {
    width: 1200px; height: 1000px; overflow: hidden;
    background: var(--backdrop);
  }
  .canvas {
    width: 1200px; height: 1000px;
    display: flex; flex-direction: column; align-items: center; justify-content: center;
    gap: 36px;
  }
  .card {
    width: 780px; height: 446px;
    background: var(--card);
    position: relative;
    overflow: hidden;
    box-shadow: 0 10px 30px rgba(0,0,0,0.35);
    font-family: "Questrial", sans-serif;
    color: var(--ink);
  }
  .brand {
    position: absolute; left: 0; right: 0;
    display: flex; align-items: center; justify-content: center; gap: 16px;
  }
  .card-front .brand { top: 130px; }
  .card-back .brand { top: 78px; }
  .brand-dot {
    width: 30px; height: 30px; border-radius: 50%;
    background: var(--accent-blue);
  }
  .brand-name {
    font-family: "Archivo", sans-serif; font-weight: 800;
    font-size: 38px; letter-spacing: 0.5px; color: var(--ink);
    white-space: nowrap;
  }

  .band {
    position: absolute; left: 0; right: 0;
    background: var(--band); color: var(--band-text);
    display: flex; align-items: center; justify-content: center;
    white-space: nowrap;
  }
  .services-band { bottom: 18px; height: 36px; font-size: 19px; letter-spacing: 0.4px; }
  .address-band { bottom: 0; height: 54px; font-size: 24px; letter-spacing: 1.2px; }

  .person {
    position: absolute; left: 78px; top: 232px;
  }
  .person-name {
    font-family: "Archivo", sans-serif; font-weight: 700;
    font-size: 27px; letter-spacing: 0.5px; color: var(--ink);
  }
  .person-role { font-size: 22px; color: var(--accent-red); margin-top: 6px; }
  .person-cred { font-size: 19px; color: var(--ink-soft); margin-top: 6px; }

  .contacts {
    position: absolute; left: 440px; top: 222px;
    list-style: none;
    font-size: 22px; letter-spacing: 0.6px; color: var(--ink-soft);
  }
  .contacts li { display: flex; align-items: center; gap: 12px; height: 32px; white-space: nowrap; }
  .contacts svg { width: 20px; height: 20px; fill: var(--ink); flex: none; }
  .contacts strong { font-family: "Archivo", sans-serif; font-weight: 700; }
</style>
</head>
<body>
<main class="canvas">

  <section class="card card-front" aria-label="Card front">
    <div class="brand">
      <span class="brand-dot"></span>
      <span class="brand-name">Larkfield Heating &amp; Cooling LLC</span>
    </div>
    <div class="band services-band">
      Heating • Cooling • Plumbing • Residential • Commercial • Industrial
    </div>
  </section>

  <section class="card card-back" aria-label="Card back">
    <div class="brand">
      <span class="brand-dot"></span>
      <span class="brand-name">Larkfield Heating &amp; Cooling LLC</span>
    </div>

    <div class="person">
      <p class="person-name">Dale Whitmore</p>
      <p class="person-role">Certified Technician</p>
      <p class="person-cred">Licensed &amp; Insured</p>
    </div>

    <ul class="contacts">
      <li>
        <svg viewBox="0 0 24 24" aria-hidden="true"><path d="M3 9c0-3 4-5 9-5s9 2 9 5v2h-5V9c-1-1-7-1-8 0v2H3zM6 13h12l2 7H4z"/></svg>
        (555) 010-0142
      </li>
      <li>
        <svg viewBox="0 0 24 24" aria-hidden="true"><path d="M4 8h3V3h10v5h3v13H4zM9 5v3h6V5zM7 12h2v2H7zm4 0h2v2h-2zm4 0h2v2h-2zM7 16h2v2H7zm4 0h2v2h-2zm4 0h2v2h-2z"/></svg>
        (555) 010-0167
      </li>
      <li>
        <svg viewBox="0 0 24 24" aria-hidden="true"><path d="M7 2h10a1 1 0 0 1 1 1v18a1 1 0 0 1-1 1H7a1 1 0 0 1-1-1V3a1 1 0 0 1 1-1zm1 2v14h8V4zm3 15v1h2v-1z"/></svg>
        (555) 010-0189
      </li>
      <li>
        <svg viewBox="0 0 24 24" aria-hidden="true"><path d="M2 5h20v14H2zm2 2v.5l8 6 8-6V7zm0 3v7h16v-7l-8 6z"/></svg>
        dale@larkfieldhc.net
      </li>
      <li>
        <svg viewBox="0 0 24 24" aria-hidden="true"><path d="M10 14a4 4 0 0 0 5.6 0l3-3a4 4 0 0 0-5.6-5.6l-1 1 1.4 1.4 1-1a2 2 0 0 1 2.8 2.8l-3 3a2 2 0 0 1-2.8 0zm4-4a4 4 0 0 0-5.6 0l-3 3a4 4 0 0 0 5.6 5.6l1-1-1.4-1.4-1 1a2 2 0 0 1-2.8-2.8l3-3a2 2 0 0 1 2.8 0z"/></svg>
        <span>www.<strong>larkfieldhc</strong>.net</span>
      </li>
    </ul>

    <div class="band address-band">48 Quillmere Lane, Ashbury Flats, OR 97999</div>
  </section>

</main>
</body>
</html>
```